Existing Website Requiring new Pages

I have an existing word press website that was built using elementor.
Website: www.tallowmerecare.com.au
I require the Vacancies page (https://www.tallowmerecare.com.au/vacancies/) to be modified to display our new properties along with minor tweaks to how the information is presented.
The vacancies to be displayed are the exactly the same as those that are located on the homepage of QPD website (https://qpd.org.au/)
The new pages that link off the Vacancies tab will require custom design.
There are roughly 8 pages/properties to be incorporated. i wish for the design to be very similar to that displayed in the following link; https://www.solquarn.com.au/vacancies/merrylands
Along with this the back end has not been updated for the last 3 years so it also requires some maintenance.
Website is in the disability industry and the custom pages will display information relative to Property Vacancies.
I have attached a ZIP file with some design guides, the information for each of the properties (which will need to be modified to show our business name Tallowmere Healthcare) and the example of how it is to look based off the Solquarn website.
If you guys have any suggestions or ideas on how to make this more presentable or possible i'm open to your ideas.
Target Market(s)
People looking for SDA properties custom built for people with a disability
Industry/Entity Type
Disability
Coding
Coded - Design and coding required
Number of Pages Required
5+ page
Look and feel
Each slider illustrates characteristics of the customer's brand and the style your logo design should communicate.

```html
<!DOCTYPE html>
<html lang="en">
<head>
<meta charset="utf-8">
<title>SDA in Greystanes – Tallowmere Healthcare</title>
<link href="https://fonts.googleapis.com/css2?family=Mulish:wght@400;600;700;800&display=swap" rel="stylesheet">
<style>
:root{
  --orange:#fbb96b;
  --orange-text:#f4ae5e;
  --pink:#e94b9c;
  --purple:#7e6bd9;
  --ink:#1f1f1f;
  --body:#333;
  --muted:#8a8a8a;
  --line:#e8e8e8;
  --green:#7cc43a;
  --dark-badge:#4a3b2a;
  --footer-bar:#1b1b1b;
  --teal:#2bb3c0;
}
*{box-sizing:border-box;margin:0;padding:0}
html,body{width:689px;height:1200px;overflow:hidden;background:#fff}
body{position:relative;font-family:'Mulish',sans-serif;color:var(--body);font-size:6.4px;line-height:9.4px}
.abs{position:absolute}
.header{left:0;top:0;width:689px;height:58px;background:#fff}
.brand{left:123px;top:14px;width:60px;color:var(--pink);font-weight:800;font-size:8.5px;line-height:10px}
.brand-dot{display:inline-block;width:8px;height:8px;border-radius:50%;background:var(--pink);vertical-align:-1px;margin-right:3px}
.nav{top:26px;font-size:4.9px;font-weight:800;letter-spacing:.3px;color:#333}
.nav.active{color:var(--orange-text)}
.hero-band{left:0;top:58px;width:689px;height:190px;background:var(--orange)}
.title{left:123px;top:100px;font-size:13.3px;line-height:16px;font-weight:700;color:var(--ink)}
.badge{top:119px;height:8px;border-radius:1.5px;font-size:4.3px;line-height:8px;font-weight:700;color:#fff;padding:0 3px}
.loc{left:123px;top:133px;font-size:6.6px;color:var(--ink)}
.ptype{left:123px;top:149px;font-size:7.6px;font-weight:800;color:var(--ink)}
.ptype-sub{left:123px;top:158px;font-size:6.6px;color:var(--ink)}
.btn{color:#fff;font-weight:700;display:flex;align-items:center;justify-content:center;border-radius:1.5px}
.btn-pink{background:var(--pink)}
.btn-purple{background:var(--purple)}
.hero-photo{left:304px;top:69px;width:261px;height:197px;border-radius:5px;
  background:linear-gradient(180deg,#c9dbe9 0%,#dfe7ea 30%,#b9a58a 48%,#8d7a66 62%,#6f7f4d 78%,#4f7a33 100%)}
.arrow{top:242px;width:13px;height:13px;border-radius:50%;background:#111}
h2.sec{left:123px;top:299px;font-size:11.8px;font-weight:700;color:var(--ink)}
.sub{font-size:7.3px;font-weight:600;color:var(--orange-text)}
.para{left:123px;width:290px;color:var(--body)}
ul.list{list-style:none}
ul.list li{padding-left:13px;position:relative}
ul.list li::before{content:"";position:absolute;left:8px;top:3px;border-left:2px solid #333;border-top:1.6px solid transparent;border-bottom:1.6px solid transparent}
.card{left:431px;top:303px;width:134px;height:329px;background:#fff;box-shadow:0 0 6px rgba(0,0,0,.08);border-radius:2px}
.card-h{font-size:7.3px;font-weight:600;color:var(--orange-text)}
.rule{height:1px;background:var(--line)}
.label{font-size:5.4px;font-weight:700;color:var(--ink)}
.field{left:438px;width:120px;border:1px solid var(--line);font-size:5.4px;color:var(--muted);padding:0 5px;display:flex;align-items:center}
.addr-card{left:123px;top:696px;width:265px;height:194px;border:1px solid var(--line)}
.map{left:124px;top:722px;width:263px;height:167px;background:linear-gradient(135deg,#eceff1,#e3e8e4 50%,#eef0ed)}
.feat{font-size:6.7px;font-weight:700;color:var(--ink)}
.footer-shadow{left:0;top:1043px;width:689px;height:4px;background:linear-gradient(180deg,rgba(0,0,0,.05),rgba(0,0,0,0))}
.foot-brand{left:129px;top:1078px;color:var(--pink);font-weight:800;font-size:11px;line-height:13px}
.foot-line{left:127px;font-size:5.5px;color:var(--muted);display:flex;align-items:center;gap:3px}
.social{left:309px;width:15px;height:15px;border-radius:50%}
.col-h{font-size:6.6px;font-weight:600;color:var(--ink);padding-left:7px;border-left:1.5px solid var(--teal);line-height:7px}
.col-item{font-size:5.5px;color:var(--muted);line-height:9.4px;border-bottom:1px solid var(--line);padding-bottom:2.5px;width:101px}
.copy{left:0;top:1170px;width:689px;height:30px;background:var(--footer-bar);color:#aaa;font-size:4.4px;display:flex;align-items:center;justify-content:center}
</style>
</head>
<body>

<header class="abs header"></header>
<div class="abs brand"><span class="brand-dot"></span>Tallowmere<br>Healthcare</div>
<nav>
  <span class="abs nav" style="left:328px">HOME</span>
  <span class="abs nav" style="left:355px">ABOUT US</span>
  <span class="abs nav active" style="left:394px">WHAT WE DO ⌄</span>
  <span class="abs nav" style="left:449px">REFERRALS</span>
  <span class="abs nav" style="left:491px">FEEDBACK</span>
  <span class="abs nav" style="left:531px">CONTACT US</span>
</nav>

<section class="abs hero-band"></section>
<h1 class="abs title">SDA in Greystanes</h1>
<span class="abs badge" style="left:123px;background:var(--green)">Featured</span>
<span class="abs badge" style="left:153px;background:var(--dark-badge)">Almost Full - Apply Now!</span>
<span class="abs badge" style="left:217px;background:var(--dark-badge)">Apply Now!</span>
<div class="abs loc"><svg width="6" height="7" viewBox="0 0 12 14" style="vertical-align:-1px;margin-right:2px"><path d="M6 13C2 8 1.5 6.5 1.5 5a4.5 4.5 0 0 1 9 0c0 1.5-.5 3-4.5 8z" fill="none" stroke="#1f1f1f" stroke-width="1.2"/><circle cx="6" cy="5" r="1.6" fill="none" stroke="#1f1f1f" stroke-width="1.1"/></svg>Greystanes</div>
<div class="abs ptype">Fully Accessible, High Physical Support</div>
<div class="abs ptype-sub">Property Type</div>
<a class="abs btn btn-pink" style="left:123px;top:179px;width:58px;height:24px;font-size:7.3px">Enquire Now</a>
<a class="abs btn btn-purple" style="left:185px;top:179px;width:92px;height:24px;font-size:7.3px;line-height:7.5px;justify-content:flex-start;padding-left:5px">
  <svg width="13" height="14" viewBox="0 0 13 14" style="margin-right:5px"><path d="M2 1h6l3 3v9H2z" fill="#fff"/><rect x="0.5" y="6" width="8" height="4" fill="var(--purple)" stroke="#fff" stroke-width=".6"/></svg>
  <span>Download<br>Property Brochure</span></a>

<div class="abs hero-photo" role="img" aria-label="Rendering of a two-storey brick SDA home with driveway, garage, gardens and trees"></div>
<svg class="abs arrow" style="left:420px" viewBox="0 0 13 13"><circle cx="6.5" cy="6.5" r="6.5" fill="#111"/><path d="M8 3.5L4.5 6.5 8 9.5z" fill="#fff"/></svg>
<svg class="abs arrow" style="left:436px" viewBox="0 0 13 13"><circle cx="6.5" cy="6.5" r="6.5" fill="#111"/><path d="M5 3.5L8.5 6.5 5 9.5z" fill="#fff"/></svg>

<main>
  <h2 class="abs sec">Description</h2>
  <p class="abs para" style="top:317px">Fully Accessible and High Physical Support apartments in Greystanes for NDIS participants looking for Specialist Disability Accommodation (SDA).</p>

  <h3 class="abs sub" style="left:123px;top:344px">Property Details</h3>
  <p class="abs para" style="top:358px">Set on 760sqm of land in the Greater Western Sydney suburb of Greystanes, this Specialist Disability Accommodation (SDA) is designed as a Fully Accessible (FA) / High Physical Support (HPS) home. The east facing home accommodation availability includes:</p>
  <ul class="abs para list" style="top:392px"><li>6 x 1 bedroom FA/HPS apartments.</li></ul>

  <h3 class="abs sub" style="left:123px;top:411px">Property Features</h3>
  <p class="abs para" style="top:425px">Located in Greater Western Sydney, QPD’s Greystanes SDA apartment complex will feature:</p>
  <ul class="abs para list" style="top:439px">
    <li>Sanctuary garden</li><li>Internal lift</li><li>Vegetable and herb garden</li>
    <li>Open space for relaxation and play</li><li>Communal area for gatherings and shared activities</li>
  </ul>
  <p class="abs para" style="top:490px">Residents are welcome to use their own Supported Independent Living (SIL) provider.</p>

  <h3 class="abs sub" style="left:123px;top:511px">Apartment Features</h3>
  <p class="abs para" style="top:525px">Each apartment is beautifully appointed with:</p>
  <ul class="abs para list" style="top:539px">
    <li>5star-rated air conditioning</li><li>Fitted-out kitchen</li><li>Bathroom with accessible facilities</li>
  </ul>

  <h3 class="abs sub" style="left:124px;top:580px">About QPD</h3>
  <p class="abs para" style="left:124px;top:594px;width:292px">Quillon Park Dwellings is a charity with extensive experience in SDA. At our heart is the desire to provide residents with SDA housing that meets their needs, in a place they call home. Our team helps NDIS participants, their families and support providers to navigate the complete SDA pathway. Call us on 1300 427 816 for more information today.</p>

  <a class="abs btn btn-pink" style="left:123px;top:647px;width:88px;height:20px;font-size:7.3px">Greystane Brochure</a>
  <a class="abs btn btn-purple" style="left:217px;top:647px;width:136px;height:20px;font-size:7.3px">
    <svg width="11" height="11" viewBox="0 0 13 14" style="margin-right:5px"><path d="M2 1h6l3 3v9H2z" fill="#fff"/><rect x="0.5" y="6" width="8" height="4" fill="var(--purple)" stroke="#fff" stroke-width=".6"/></svg>Download Property Brochure</a>

  <div class="abs addr-card"></div>
  <span class="abs sub" style="left:134px;top:703px">Address</span>
  <span class="abs" style="left:267px;top:704px;color:var(--ink)"><b>Suburb:</b> Greystanes</span>
  <span class="abs" style="left:339px;top:704px;color:var(--ink)"><b>State:</b> NSW</span>
  <div class="abs map" role="img" aria-label="Street map of Greystanes and surrounding suburbs with a property marker"></div>

  <div class="abs rule" style="left:123px;top:916px;width:293px"></div>
  <h3 class="abs sub" style="left:123px;top:935px">Features</h3>

  <svg class="abs" style="left:123px;top:952px" width="13" height="12" viewBox="0 0 13 12" fill="none" stroke="var(--orange-text)" stroke-width=".8"><rect x=".5" y=".5" width="12" height="6"/><path d="M2 4.5h9M3 8v3M5 8v3M7 8v3M9 8v3"/></svg>
  <span class="abs feat" style="left:143px;top:953px">Air Conditioning</span>
  <svg class="abs" style="left:233px;top:952px" width="13" height="10" viewBox="0 0 13 10" fill="none" stroke="var(--orange-text)" stroke-width=".8"><rect x=".5" y=".5" width="12" height="9"/><rect x="2" y="2" width="6" height="6"/><path d="M10 3v1M10 6v1"/></svg>
  <span class="abs feat" style="left:251px;top:953px">Microwave</span>
  <svg class="abs" style="left:343px;top:953px" width="13" height="9" viewBox="0 0 13 9" fill="none" stroke="var(--orange-text)" stroke-width=".9"><path d="M1 3.5a8 8 0 0 1 11 0M3 5.5a5 5 0 0 1 7 0M5 7.3a2 2 0 0 1 3 0"/></svg>
  <span class="abs feat" style="left:361px;top:953px">WiFi</span>

  <svg class="abs" style="left:123px;top:974px" width="13" height="12" viewBox="0 0 13 12" fill="none" stroke="var(--orange-text)" stroke-width=".8"><circle cx="6.5" cy="6" r="5"/><circle cx="6.5" cy="6" r="2.5"/></svg>
  <span class="abs feat" style="left:143px;top:975px">Dryer</span>
  <svg class="abs" style="left:235px;top:973px" width="10" height="13" viewBox="0 0 10 13" fill="none" stroke="var(--orange-text)" stroke-width=".8"><rect x=".5" y=".5" width="9" height="12"/><path d="M.5 4.5h9M2 2v1.5M2 6v2"/></svg>
  <span class="abs feat" style="left:251px;top:974px">Refrigerator</span>

  <svg class="abs" style="left:123px;top:995px" width="13" height="11" viewBox="0 0 13 11" fill="none" stroke="var(--orange-text)" stroke-width=".8"><path d="M1 10.5h11M2 10L1 4M4 10l-1-7M6.5 10V1M9 10l1-7M11 10l1-6"/></svg>
  <span class="abs feat" style="left:143px;top:996px">Lawn</span>
  <svg class="abs" style="left:234px;top:994px" width="12" height="13" viewBox="0 0 12 13" fill="none" stroke="var(--orange-text)" stroke-width=".8"><rect x=".5" y=".5" width="11" height="12"/><path d="M.5 3h11"/><circle cx="6" cy="8" r="3"/></svg>
  <span class="abs feat" style="left:251px;top:996px">Washer</span>
</main>

<aside class="abs card">
  <div class="abs card-h" style="left:7px;top:8px">Contact Information</div>
  <span class="abs btn btn-pink" style="left:7px;top:21px;width:48px;height:10px;font-size:5.4px">View Listings</span>
  <div class="abs rule" style="left:7px;top:38px;width:122px"></div>
  <svg class="abs" style="left:8px;top:46px" width="24" height="24" viewBox="0 0 24 24"><rect width="24" height="24" rx="2" fill="#ececec"/><circle cx="12" cy="9.5" r="3.8" fill="none" stroke="#bbb" stroke-width="1"/><path d="M5 20c1.5-4 4-5 7-5s5.5 1 7 5" fill="none" stroke="#bbb" stroke-width="1"/></svg>
  <span class="abs" style="left:38px;top:53px;font-size:6.4px;color:var(--ink)">info@qpd.org.au</span>
  <div class="abs rule" style="left:7px;top:77px;width:122px"></div>
  <div class="abs card-h" style="left:7px;top:86px">Enquire About This Property</div>
</aside>
<span class="abs label" style="left:438px;top:406px">Name</span>
<div class="abs field" style="top:416px;height:19px">Enter your name</div>
<span class="abs label" style="left:438px;top:440px">Phone</span>
<div class="abs field" style="top:449px;height:19px">Enter your phone</div>
<span class="abs label" style="left:438px;top:473px">Email</span>
<div class="abs field" style="top:483px;height:18px">Enter your email</div>
<span class="abs label" style="left:438px;top:506px">I'm a</span>
<div class="abs field" style="top:516px;height:19px;justify-content:space-between">Select<svg width="6" height="4" viewBox="0 0 6 4"><path d="M.5.5L3 3 5.5.5" fill="none" stroke="#888" stroke-width=".7"/></svg></div>
<span class="abs label" style="left:438px;top:540px">Message</span>
<div class="abs field" style="top:550px;height:39px;align-items:flex-start;padding-top:5px;line-height:7.2px">Hello, I am interested in<br>[SDA in Greystanes]</div>
<a class="abs btn btn-pink" style="left:438px;top:597px;width:77px;height:18px;font-size:6.4px">Request Information</a>

<footer>
  <div class="abs footer-shadow"></div>
  <div class="abs foot-brand">Tallowmere<br>Healthcare</div>
  <div class="abs foot-line" style="top:1131px"><svg width="6" height="5" viewBox="0 0 6 5" fill="none" stroke="var(--pink)" stroke-width=".6"><rect x=".3" y=".3" width="5.4" height="4.4"/><path d="M.3.3L3 2.8 5.7.3"/></svg>Email: info@tallowmerecare.com.au</div>
  <div class="abs foot-line" style="top:1140px"><svg width="6" height="6" viewBox="0 0 6 6"><path d="M1 .3l1.2 1.3-.6.9a4 4 0 0 0 1.9 1.9l.9-.6L5.7 5 5 5.7C2.5 5.5.5 3.5.3 1z" fill="var(--pink)"/></svg>Phone: +61 0400 118 236</div>
  <div class="abs foot-line" style="top:1150px"><svg width="6" height="6" viewBox="0 0 6 6" fill="none" stroke="var(--pink)" stroke-width=".6"><circle cx="3" cy="3" r="2.6"/><path d="M3 1.5V3l1 .8"/></svg>Operating Hours: 9AM To 5PM Monday - Friday</div>

  <div class="abs social" style="top:1067px;background:#7b2d8e"></div>
  <div class="abs social" style="top:1085px;background:#2a4d8f"></div>
  <div class="abs social" style="top:1103px;background:#222"></div>
  <div class="abs social" style="top:1121px;background:#1b6fa8"></div>

  <div class="abs col-h" style="left:350px;top:1063px">ACCOMMODATION</div>
  <div class="abs" style="left:350px;top:1076px">
    <div class="col-item">Supported Independent Living (SIL)</div>
    <div class="col-item" style="padding-top:2px">Specialist Disability<br>Accommodation (SDA)</div>
    <div class="col-item" style="padding-top:2px">Short term Accommodation<br>(Respite)</div>
    <div class="col-item" style="padding-top:2px">Vacancies</div>
  </div>
  <div class="abs col-h" style="left:461px;top:1063px">WHAT WE DO</div>
  <div class="abs" style="left:461px;top:1076px">
    <div class="col-item">In Home Care</div>
    <div class="col-item" style="padding-top:2px">Social &amp; Community Services</div>
    <div class="col-item" style="padding-top:2px">Therapeutic Supports</div>
    <div class="col-item" style="padding-top:2px">Support Coordination</div>
    <div class="col-item" style="padding-top:2px">Home Modifications</div>
  </div>
  <div class="abs copy">© Copyright 2021 | Tallowmere Healthcare | All Rights Reserved.</div>
</footer>

</body>
</html>
```